皆さん素敵な提案をありがとうございました!色々迷いましたが最終的にこの提案を採用させて頂きます。理由このデザインが一番弊社商品のイメージに適しているからです。
皆様、すばらしいご提案ありがとうございました。
今回はご縁がありませんでしたが、またの機会にお願いできればと考えております。
この度は、弊社にご応募いただきまして誠にありがとうございます。
より希望のデザインへ近つくため、以下新しくデザイン方針を更新・修正致します。
まだ製作中の商品で詳しい情報は少ないと思いますが、お互いの齟齬を少なくするためにも、ご不明な点などございましたら、何なりとお申し付けください。
・パッケージ
サイズ:100×195(H)
白いジップロック付きのアルミ袋になります
イメージ:https://www.toriyose-ichiba.jp/dp/K93TZW571Q/
(こちらは弊社販売中の別ブランド商品です。パッケージは同じものを使用します。ただ今回の商品は新ブランドの商品になるので、ラベルのデザインにおいて参考しなくて結構です、あくまでもパッケージのイメージとして参考してください。)
・配色、カラー
まずは下の検索ページを確認ください:
https://www.toriyose-ichiba.jp/search/q=mx_rq_lt_kw_d_3_7?__lc_ja_JP=%E3%82%AB%E3%82%BF%E3%82%AB%E3%83%8A&scope=category-alias%3Dwell&query=%E3%82%B7%E3%83%A3%E3%83%B3%E3%83%94%E3%83%8B%E3%82%AA%E3%83%B3&prefix=%E3%82%B7%E3%83%A3%E3%83%B3%E3%83%94%2Call%2C517&sid=72HRW03KLNUB8&node=c%3A904127635%2Cq%3A%E3%82%B7%E3%83%A3%E3%83%B3%E3%83%94%E3%83%8B%E3%82%AA%E3%83%B3
他社商品と差別化するため、青は避けて頂ければと思います。
想定はオレンジ〜茶色(柿色)、もしくはピンクです。
添付ファイルにてランディングページの設計イメージを添付致します。
また、白アルミのパッケージから考えると、純白のベースは目立たないという心配で、デザイン方針の「白ベース」削除致します。
ただしアイボリーやオフホワイトなどの色、もしくプレームとの組み合わせですとOKです。
あくまでも、パッケージの上からラベルが見やすいイメージでお願い致します。
以上、お手数をおかけしますが、ご検討の程よろしくお願い致します。

```html
<!DOCTYPE html>
<html lang="ja">
<head>
<meta charset="utf-8">
<title>シャンピニオン ラベル案</title>
<link rel="stylesheet" href="https://fonts.googleapis.com/css2?family=Shippori+Mincho+B1:wght@800&family=Noto+Sans+JP:wght@400;500;700&display=swap">
<style>
  :root {
    --orange: #f08a1c;
    --orange-deep: #e27410;
    --orange-light: #f7a94a;
    --parchment: #f6e3c0;
    --parchment-pale: #fbefd8;
    --ink: #111111;
    --brown: #4a2a10;
    --white: #ffffff;
    --pill-line: #b9a58a;
    --pill-text: #8a7a66;
    --page: #ffffff;
  }
  * { box-sizing: border-box; margin: 0; padding: 0; }
  html, body { width: 1200px; height: 866px; overflow: hidden; background: var(--page); }
  body { position: relative; font-family: "Noto Sans JP", sans-serif; }

  .label {
    position: absolute; top: 40px; width: 532px; height: 770px; overflow: hidden;
  }
  .label--orange { left: 30px; background: linear-gradient(90deg, var(--orange-deep), var(--orange) 30%, var(--orange) 70%, var(--orange-deep)); }
  .label--cream { left: 636px; background: var(--parchment); }

  .stripe { position: absolute; top: 0; bottom: 0; }
  .label--orange .stripe { background: linear-gradient(90deg, var(--parchment), var(--parchment-pale), var(--parchment)); width: 40px; }
  .label--orange .stripe--left { left: 14px; }
  .label--orange .stripe--right { right: 56px; }

  .label--cream .panel {
    position: absolute; top: 0; bottom: 0; left: 54px; right: 60px;
    background: linear-gradient(90deg, var(--orange-deep), var(--orange) 25%, var(--orange-light) 50%, var(--orange) 75%, var(--orange-deep));
  }
  .label--cream .stripe { width: 14px; background: var(--orange); }
  .label--cream .stripe--left { left: 22px; }
  .label--cream .stripe--right { right: 28px; }

  .tagline {
    position: absolute; top: 96px; left: 0; right: 0; text-align: center;
    color: var(--white); font-weight: 500; font-size: 29px; line-height: 1.3; letter-spacing: 2px;
  }
  .title-band {
    position: absolute; top: 230px; left: 0; right: 0; height: 96px;
    background: var(--white); display: flex; align-items: center; justify-content: center;
  }
  .label--cream .title-band { background: linear-gradient(90deg, transparent, var(--parchment-pale) 12%, var(--white) 30%, var(--white) 70%, var(--parchment-pale) 88%, transparent); }
  .title {
    font-family: "Shippori Mincho B1", serif; font-weight: 800; font-size: 66px;
    color: var(--ink); letter-spacing: 0; white-space: nowrap;
  }
  .concern {
    position: absolute; top: 340px; left: 0; right: 0; text-align: center;
    color: var(--white); font-weight: 500; font-size: 36px; line-height: 1.25; letter-spacing: 1px;
  }
  .photo {
    position: absolute; top: 436px; left: 20px; right: 20px; height: 180px;
    background: radial-gradient(ellipse at center, #ffffff 0%, #ffffff 40%, #fbefe2 60%, rgba(255,255,255,0) 72%);
  }
  .photo::after {
    content: ""; position: absolute; left: 28%; top: 24%; width: 44%; height: 56%; border-radius: 50%;
    background: radial-gradient(ellipse at center, #c9a98a, #e9dccd 60%, rgba(255,255,255,0) 75%);
  }
  .ingredients {
    position: absolute; top: 645px; left: 0; right: 0; text-align: center;
    color: var(--brown); font-weight: 700; font-size: 19px; line-height: 1.4;
  }
  .contents {
    position: absolute; top: 734px; left: 50%; transform: translateX(-50%);
    border: 1.5px solid var(--pill-line); border-radius: 10px; padding: 0 14px;
    background: rgba(255,255,255,0.35);
    color: var(--pill-text); font-size: 13px; line-height: 20px; white-space: nowrap;
  }
  .label--orange .tagline, .label--orange .concern, .label--orange .ingredients,
  .label--orange .contents { margin-left: -20px; }
  .label--orange .title-band { }
</style>
</head>
<body>
  <section class="label label--orange">
    <div class="stripe stripe--left"></div>
    <div class="stripe stripe--right"></div>
    <p class="tagline">お悩み解決<br>サポートサプリ</p>
    <div class="title-band"><h1 class="title">シャンピニオン</h1></div>
    <p class="concern">気になる<br>口臭・体臭に</p>
    <div class="photo" role="img" aria-label="シャンピニオン(マッシュルーム)の写真"></div>
    <p class="ingredients">シャンピニオン<br>緑茶、乳酸菌成分配合</p>
    <p class="contents">1袋60粒入り</p>
  </section>

  <section class="label label--cream">
    <div class="panel"></div>
    <div class="stripe stripe--left"></div>
    <div class="stripe stripe--right"></div>
    <p class="tagline">お悩み解決<br>サポートサプリ</p>
    <div class="title-band"><h1 class="title">シャンピニオン</h1></div>
    <p class="concern">気になる<br>口臭・体臭に</p>
    <div class="photo" role="img" aria-label="シャンピニオン(マッシュルーム)の写真"></div>
    <p class="ingredients">シャンピニオン<br>緑茶、乳酸菌成分配合</p>
    <p class="contents">1袋60粒入り</p>
  </section>
</body>
</html>
```